Online Prescription Eyeglass Lens Company Needs a Website

*Update new name to Glintwell. Thx

We are eye doctors with a lab that need a website for a new company based in Southern California called Glintwell. We replace old prescription lenses with new ones next day for most lenses. Patients select the lenses and give us the prescription. We then send a box with a prepaid shipping label. Place the frames in the box and drop them in the mail to our lab. We will custom make new lenses, fit them back into your frames and send them back to you. We would like to compete with www.spectrafold.com and offer affordable lenses for single vision, bifocal, progressive, sunglass lenses at an affordable price with next day shipping.
Updates

Hi Designers, We have a new name called Glintwell. Can we have the website design reflect the new name and we'll pick our favorites. Thx

Update: The new name is Brightmoor . I have not made very many changes or feedback to the submissions because we were bidding for a .com. We won and our new name is Brightmoor . This is the last name change.. Please have the website reflect the new name and I'll be providing feedback on the websites . ( I have a separate project for the logo people are working on, so don't worry about creating a logo). Look forward to the submissions. Thanks everyone.

Hi, Just leave the name as Glintwell for now. I will narrow down top designs tonight. Thx

Target Market(s)

Anyone that wears prescription or nonprescription glasses or sunglasses that want next day shipping.

Industry/Entity Type

Eyewear

Number of Pages Required

4 page

Font styles to use
Serif

Colors

Designer to choose colors to be used in the design.

Requirements
Must have
• I need a website that can compete with https://www.spectrafold.com/.
• We are different from spectrafold because we can offer same day service or next day shipping.
• It needs to have website that offers the lenses available listed below.
• Needs to be able to upload a prescription and payment feature.
• Pictures of different types of options with small info about each lens option.
• Template Pricing (just use numbers from $79-$179 for now)
• SINGLE VISION LENSES
• HIGH INDEX LENSES
• READING LENSES
• DIGITAL HD PROGRESSIVE LENSES
• RX & NON-RX SUNGLASSES
• RX & NON-RX POLARIZED SUNGLASSES
• COMPUTER LENSES
• TRANSITION LENSES
• BI-FOCAL LENSES

```html
<!DOCTYPE html>
<html lang="en">
<head>
<meta charset="utf-8">
<title>Glintwell — Contact Lenses</title>
<link rel="stylesheet" href="https://fonts.googleapis.com/css2?family=Poppins:wght@300;400;500;600;700&display=swap">
<style>
:root{
  --blue:#1b9be0;
  --blue-dark:#0f86c8;
  --ink:#1f2430;
  --text:#666c77;
  --muted:#9aa0aa;
  --line:#e3e6ea;
  --yellow:#f7ec8a;
  --yellow-light:#fdf7c9;
  --gray-bg:#f3f4f6;
  --footer:#2b303b;
  --footer-bar:#232731;
  --footer-text:#aeb3bd;
  --white:#ffffff;
  --star:#f5a623;
}
*{box-sizing:border-box;margin:0;padding:0}
html,body{width:1200px;height:4072px;overflow:hidden}
body{font-family:'Poppins',sans-serif;color:var(--text);background:var(--white);position:relative}
.abs{position:absolute}
.btn{position:absolute;display:flex;align-items:center;justify-content:center;font-size:12px;font-weight:600;letter-spacing:.5px;text-transform:uppercase}
.btn-dark{background:var(--ink);color:var(--white)}
.btn-blue{background:var(--blue);color:var(--white)}
.btn-white{background:var(--white);color:var(--ink)}

/* header */
.site-header{position:absolute;left:0;top:0;width:1200px;height:90px;background:var(--white)}
.brand{position:absolute;left:87px;top:28px;display:flex;align-items:center;gap:10px;font-size:22px;font-weight:700;color:var(--ink);letter-spacing:.5px}
.brand-dot{width:26px;height:26px;border-radius:50%;background:var(--blue)}
.main-nav{position:absolute;left:430px;top:36px;display:flex;gap:36px;font-size:12px;font-weight:500;color:var(--text);text-transform:uppercase}
.main-nav .active{color:var(--ink);border-bottom:2px solid var(--blue);padding-bottom:4px}
.sign-in{left:1030px;top:29px;width:70px;height:32px}

/* hero */
.hero{position:absolute;left:0;top:90px;width:1200px;height:589px;background:linear-gradient(90deg,var(--yellow-light) 0%,var(--yellow) 100%);overflow:hidden}
.hero-photo{position:absolute;left:520px;top:0;width:680px;height:589px;background:radial-gradient(ellipse at 60% 60%,#4f7fbf 0%,#6a92c8 35%,rgba(247,236,138,0) 70%)}
.hero-price{position:absolute;left:87px;top:200px;font-size:26px;font-weight:500;color:var(--ink)}
.hero-title{position:absolute;left:87px;top:236px;font-size:60px;font-weight:700;color:var(--ink);letter-spacing:1px}
.hero-title span{color:var(--blue)}
.hero-sub{position:absolute;left:87px;top:302px;font-size:16px;font-weight:500;color:var(--ink)}
.hero-btn{left:87px;top:334px;width:176px;height:46px}
.slider-arrow{position:absolute;top:270px;width:26px;height:46px;background:rgba(255,255,255,.85);display:flex;align-items:center;justify-content:center}
.scroll-down{position:absolute;left:575px;top:654px;width:50px;height:50px;border-radius:50%;background:var(--white);box-shadow:0 2px 8px rgba(0,0,0,.12);display:flex;align-items:center;justify-content:center;z-index:2}

/* shipping band */
.ship-band{position:absolute;left:0;top:679px;width:1200px;height:141px;background:var(--blue)}
.ship-icon{position:absolute;left:87px;top:36px}
.ship-text{position:absolute;left:198px;top:54px;font-size:25px;font-weight:600;color:var(--white);letter-spacing:.3px}
.ship-btn{left:968px;top:45px;width:142px;height:48px}

/* process */
.section-title{position:absolute;width:1200px;left:0;text-align:center;font-size:26px;font-weight:600;color:var(--ink);letter-spacing:.5px}
.timeline{position:absolute;left:599px;top:1005px;width:2px;height:692px;background:var(--line)}
.step-num{position:absolute;width:38px;height:38px;border-radius:50%;background:#e5f3fc;color:var(--blue);font-size:13px;font-weight:600;display:flex;align-items:center;justify-content:center}
.step-title{position:absolute;font-size:15px;font-weight:600;color:var(--ink);text-transform:uppercase}
.step-text{position:absolute;width:330px;font-size:13px;line-height:26px;color:var(--text)}
.right{text-align:right}
.step-icon{position:absolute}

/* cta band */
.cta-band{position:absolute;left:0;top:1805px;width:1200px;height:226px;background:linear-gradient(90deg,#1590d4,var(--blue))}
.cta-title{position:absolute;left:87px;top:70px;font-size:28px;font-weight:600;color:var(--white)}
.cta-sub{position:absolute;left:87px;top:128px;font-size:14px;color:#d9effb}
.cta-btn{left:950px;top:93px;width:160px;height:44px}

/* why choose */
.why-photo{position:absolute;left:87px;top:2186px;width:429px;height:393px;background:linear-gradient(135deg,#d9d6d3 0%,#b7aca4 50%,#e7e6e4 100%)}
.why-accent{position:absolute;left:87px;top:2186px;width:166px;height:5px;background:var(--blue)}
.why-badge{position:absolute;left:429px;top:2451px;width:120px;height:120px;border-radius:50%;background:#c9c9c9;border:6px solid var(--white)}
.why-title{position:absolute;left:608px;top:2195px;font-size:26px;font-weight:600;color:var(--ink)}
.why-text{position:absolute;left:608px;top:2250px;width:500px;font-size:13px;line-height:24px}
.lens-list{position:absolute;font-size:12px;color:var(--text);text-transform:uppercase;list-style:none}
.lens-list li{height:32.5px;display:flex;align-items:center;gap:10px}
.lens-list li::before{content:"";width:6px;height:6px;border-radius:50%;background:var(--line)}
.lens-list li.current{color:var(--ink);font-weight:500}
.lens-list li.current::before{background:var(--blue)}
.why-btn{left:608px;top:2517px;width:158px;height:43px}

/* our lenses */
.glass-icon{position:absolute;left:87px;top:2728px;width:60px;height:60px;border-radius:50%;background:#e5f3fc;display:flex;align-items:center;justify-content:center}
.glass-title{position:absolute;left:87px;top:2798px;font-size:26px;font-weight:600;color:var(--ink)}
.glass-text{position:absolute;left:87px;top:2850px;width:510px;font-size:13px;line-height:24px}
.glass-btn{left:87px;top:2957px;width:163px;height:43px}
.glass-photo{position:absolute;left:624px;top:2715px;width:516px;height:299px;background:radial-gradient(ellipse at 50% 60%,#8fd3e6 0%,#3c73ad 40%,rgba(255,255,255,0) 72%)}

/* testimonials */
.testimonials{position:absolute;left:0;top:3109px;width:1200px;height:529px;background:var(--gray-bg)}
.t-arrows{position:absolute;left:1024px;top:104px}
.t-card{position:absolute;top:176px;width:331px;height:250px;background:var(--white);box-shadow:0 3px 14px rgba(0,0,0,.05)}
.t-stars{position:absolute;left:32px;top:26px;color:var(--star);font-size:15px;letter-spacing:3px}
.t-quote{position:absolute;left:32px;top:60px;width:270px;font-size:12px;line-height:20px;font-style:italic;color:var(--text)}
.t-avatar{position:absolute;left:32px;top:176px;width:44px;height:44px;border-radius:50%;background:linear-gradient(135deg,#c8ccd2,#8a9099)}
.t-name{position:absolute;left:90px;top:188px;font-size:13px;font-weight:600;color:var(--ink)}

/* footer */
.site-footer{position:absolute;left:0;top:3638px;width:1200px;height:375px;background:var(--footer);color:var(--footer-text)}
.f-head{position:absolute;top:73px;font-size:15px;font-weight:500;color:var(--white)}
.f-links{position:absolute;top:115px;list-style:none;font-size:12px}
.f-links li{height:36px}
.f-links li::before{content:"› ";}
.f-contact{position:absolute;left:559px;top:115px;font-size:12px;list-style:none}
.f-contact li{display:flex;gap:12px;margin-bottom:24px;line-height:20px}
.f-contact .ico{width:14px;height:14px;border-radius:50%;background:var(--blue);flex:none;margin-top:3px}
.social{position:absolute;left:855px;top:115px;display:flex;gap:14px}
.social span{width:30px;height:30px;border-radius:50%;background:#3a404c;display:block}
.mail-title{position:absolute;left:855px;top:190px;font-size:15px;font-weight:500;color:var(--white)}
.mail-form{position:absolute;left:855px;top:230px;width:255px;height:44px;background:var(--white);display:flex;align-items:center;justify-content:space-between;padding:0 14px;font-size:11px;color:var(--muted)}
.footer-bar{position:absolute;left:0;top:4013px;width:1200px;height:59px;background:var(--footer-bar);color:var(--footer-text);font-size:12px}
.copyright{position:absolute;left:87px;top:21px}
.pay-cards{position:absolute;right:90px;top:14px;display:flex;gap:8px}
.pay-cards span{width:46px;height:30px;border-radius:4px;background:#dfe3e8;display:block}
.to-top{position:absolute;left:1110px;top:4000px;width:40px;height:40px;border-radius:50%;background:var(--blue);display:flex;align-items:center;justify-content:center;color:var(--white);font-size:16px}
</style>
</head>
<body>

<header class="site-header">
  <div class="brand"><span class="brand-dot"></span>GLINTWELL</div>
  <nav class="main-nav">
    <span class="active">Home</span><span>Features</span><span>Contact Lenses</span><span>Process</span><span>Our Lab</span><span>Contact Us</span>
  </nav>
  <span class="btn btn-blue sign-in">Sign In</span>
</header>

<section class="hero">
  <div class="hero-photo" role="img" aria-label="Photo of a smiling woman in a denim shirt adjusting her glasses"></div>
  <p class="hero-price">From $79-$179</p>
  <h1 class="hero-title">CONTACT <span>LENSES</span></h1>
  <p class="hero-sub">Let us Help You Discover The Freedom And Benefits Of</p>
  <span class="btn btn-dark hero-btn">Choose Your Lenses</span>
  <div class="slider-arrow" style="left:0"><svg width="8" height="12"><path d="M6 1 1 6l5 5" fill="none" stroke="#888" stroke-width="1.5"/></svg></div>
  <div class="slider-arrow" style="right:0"><svg width="8" height="12"><path d="M2 1l5 5-5 5" fill="none" stroke="#333" stroke-width="1.5"/></svg></div>
</section>
<div class="scroll-down"><svg width="12" height="16"><path d="M6 1v13M1 9l5 5 5-5" fill="none" stroke="#1f2430" stroke-width="1.6"/></svg></div>

<section class="ship-band">
  <svg class="ship-icon" width="90" height="66" viewBox="0 0 90 66" fill="none" stroke="#fff" stroke-width="3">
    <rect x="4" y="10" width="48" height="36"/><path d="M52 22h18l12 14v10H52z"/><circle cx="20" cy="50" r="7" fill="#1b9be0"/><circle cx="68" cy="50" r="7" fill="#1b9be0"/>
  </svg>
  <p class="ship-text">WE OFFER SAME DAY SERVICE OR NEXT DAY SHIPPING</p>
  <span class="btn btn-white ship-btn">Let's Get Started</span>
</section>

<h2 class="section-title" style="top:920px">HOW GLINTWELL WORKS</h2>
<div class="timeline"></div>

<div class="step-icon" role="img" aria-label="Line icon of a person working at a computer" style="left:380px;top:1018px;width:130px;height:122px">
  <svg width="130" height="122" viewBox="0 0 130 122" fill="none" stroke="#1f2430" stroke-width="3"><rect x="58" y="42" width="64" height="46" rx="4" fill="#1b9be0" stroke="none"/><path d="M4 110h122M30 88h60"/></svg>
</div>
<span class="step-num" style="left:687px;top:1013px">01</span>
<p class="step-title" style="left:687px;top:1060px">Pick your lenses.</p>
<p class="step-text" style="left:687px;top:1100px">Aenean sollicitudin, lorem quis bibendum auctor, nisi elit consequat ipsum nec sagittis...</p>

<span class="step-num" style="left:470px;top:1189px">02</span>
<p class="step-title right" style="left:180px;top:1242px;width:328px">Send us your frames.</p>
<p class="step-text right" style="left:178px;top:1282px">Aenean sollicitudin, lorem quis bibendum auctor, nisi elit consequat ipsum nec sagittis...</p>
<svg class="step-icon" style="left:687px;top:1195px" width="120" height="122" viewBox="0 0 120 122" fill="none" stroke="#1f2430" stroke-width="3">
  <path d="M10 50a24 24 0 0 1 48 0v32H10z"/><path d="M58 26h44v56H58"/><path d="M34 82v36"/><path d="M78 50V12"/><path d="M78 12h18v12H78z" fill="#1b9be0" stroke="#1b9be0"/><path d="M20 58v14M28 58v14M36 58v14"/>
</svg>

<svg class="step-icon" role="img" aria-label="Eyeglasses icon" style="left:380px;top:1385px" width="130" height="108" viewBox="0 0 130 108" fill="none" stroke="#1f2430" stroke-width="4">
  <circle cx="32" cy="66" r="26"/><circle cx="98" cy="66" r="26"/><path d="M58 62q7-8 14 0M8 56 14 10M122 56l-6-46"/><path d="M108 80a14 14 0 0 0 8-10" stroke="#1b9be0"/>
</svg>
<span class="step-num" style="left:687px;top:1368px">03</span>
<p class="step-title" style="left:687px;top:1421px">We re lens your glasses.</p>
<p class="step-text" style="left:687px;top:1461px">Aenean sollicitudin, lorem quis bibendum auctor, nisi elit consequat ipsum nec sagittis...</p>

<span class="step-num" style="left:470px;top:1550px">04</span>
<p class="step-title right" style="left:180px;top:1603px;width:328px">Sight, sealed, delivered.</p>
<p class="step-text right" style="left:178px;top:1643px">Aenean sollicitudin, lorem quis bibendum auctor, nisi elit consequat ipsum nec sagittis...</p>
<svg class="step-icon" style="left:687px;top:1569px" width="160" height="104" viewBox="0 0 160 104" fill="none" stroke="#1f2430" stroke-width="3.5">
  <rect x="4" y="6" width="96" height="74"/><path d="M100 30h30l24 26v24h-54z"/><circle cx="32" cy="86" r="11" fill="#fff"/><circle cx="124" cy="86" r="11" fill="#fff"/><path d="M36 46l16-14 16 14v20H36z" fill="#1b9be0" stroke="#1b9be0"/>
</svg>

<section class="cta-band">
  <h2 class="cta-title">REPLACE OLD PRESCRIPTION LENSES WITH NEW ONES</h2>
  <p class="cta-sub">Find out what type of contact lenses are right for you, and the benefits which they can bring.</p>
  <span class="btn btn-white cta-btn">Let's Get Started</span>
</section>

<div class="why-photo" role="img" aria-label="Close-up photo of a person putting in a contact lens"></div>
<div class="why-accent"></div>
<div class="why-badge"></div>
<h2 class="why-title">WHY CHOOSE US</h2>
<p class="why-text">Duis sed odio sit amet nibh vulputate cursus a sit amet mauris. Morbi accumsan ipsum velit. Nam nec tellus a odio tincidunt auctor...</p>
<ul class="lens-list" style="left:608px;top:2333px">
  <li class="current">Single Vision Lenses</li><li>High Index Lenses</li><li>Reading Lenses</li><li>Digital HD Progressive Lenses</li><li>RX &amp; Non-RX Sunglasses</li>
</ul>
<ul class="lens-list" style="left:869px;top:2333px">
  <li>RX &amp; Non-RX Polarized Sunglasses</li><li>Computer Lenses</li><li>Transition Lenses</li><li>Bi-Focal Lenses</li>
</ul>
<span class="btn btn-blue why-btn">View All Details</span>

<div class="glass-icon"><svg width="30" height="16" viewBox="0 0 30 16" fill="none" stroke="#1b9be0" stroke-width="2"><path d="M2 12h26M5 12 9 3h12l4 9"/></svg></div>
<h2 class="glass-title">OUR LENSES GLASS</h2>
<p class="glass-text">Aenean sollicitudin, lorem quis bibendum auctor, nisi elit consequat ipsum, nec sagittis sem nibh id elit. Duis sed odio sit amet nibh vulputate cursus a sit amet mauris. Morbi accumsan ipsum velit...</p>
<span class="btn btn-blue glass-btn">View All Details</span>
<div class="glass-photo" role="img" aria-label="Photo of blue gradient eyeglass frames"></div>

<section class="testimonials">
  <h2 class="section-title" style="top:96px;font-size:25px">CUSTOMR'S TESTIMONIALS</h2>
  <svg class="t-arrows" width="90" height="20" viewBox="0 0 90 20" fill="none" stroke-width="2"><path d="M26 10H4m6-6-6 6 6 6" stroke="#9aa0aa"/><path d="M40 10h46m-6-6 6 6-6 6" stroke="#1b9be0"/></svg>
  <article class="t-card" style="left:87px">
    <div class="t-stars">★★★★★</div>
    <p class="t-quote">"Consequat vitae eleifend ac enim aliquam lorem ante dapibu. In viverra quis feugiat a, tellus phasellus lorem ipsum dolor sit amet is some dummy text for filler."</p>
    <div class="t-avatar"></div><p class="t-name">Owen Hartley</p>
  </article>
  <article class="t-card" style="left:434px">
    <div class="t-stars">★★★★★</div>
    <p class="t-quote">"Consequat vitae eleifend ac enim aliquam lorem ante dapibu. In viverra quis feugiat a, tellus phasellus lorem ipsum dolor sit amet is some dummy text for filler."</p>
    <div class="t-avatar"></div><p class="t-name">Maya Ellison</p>
  </article>
  <article class="t-card" style="left:782px">
    <div class="t-stars">★★★★★</div>
    <p class="t-quote">"Consequat vitae eleifend ac enim aliquam lorem ante dapibu. In viverra quis feugiat a, tellus phasellus lorem ipsum dolor sit amet is some dummy text for filler."</p>
    <div class="t-avatar"></div><p class="t-name">Felix Navarro</p>
  </article>
</section>

<footer class="site-footer">
  <h3 class="f-head" style="left:87px">Quick Links</h3>
  <ul class="f-links" style="left:87px"><li>Home</li><li>Features</li><li>Contact Lenses</li><li>Process</li><li>Our lab</li><li>Contact Us</li></ul>
  <h3 class="f-head" style="left:329px">Help &amp; Support</h3>
  <ul class="f-links" style="left:329px"><li>Track Order</li><li>Contact</li><li>FAQs</li><li>Returns</li><li>Terms</li><li>Privacy</li></ul>
  <h3 class="f-head" style="left:559px">Contact information</h3>
  <ul class="f-contact">
    <li><span class="ico"></span>Some address line goes here<br>city name country</li>
    <li><span class="ico"></span>Telephone : +1 555 014 2290</li>
    <li><span class="ico"></span>Email : care@glintwell.com</li>
    <li><span class="ico"></span>Web : www.glintwell.com</li>
  </ul>
  <h3 class="f-head" style="left:855px">Stay Connected</h3>
  <div class="social"><span></span><span></span><span></span><span></span><span></span></div>
  <h3 class="mail-title">Join our mailing list</h3>
  <div class="mail-form">Enter email address<svg width="16" height="16" viewBox="0 0 16 16"><path d="M1 8 15 1 11 15 8 9z" fill="#1b9be0"/></svg></div>
</footer>
<div class="footer-bar">
  <p class="copyright">© Copyright 2017 &nbsp;|&nbsp; All Rights Reserved</p>
  <div class="pay-cards"><span></span><span></span><span></span><span></span><span></span></div>
</div>
<div class="to-top">↑</div>

</body>
</html>
```